Educational Institution needs a new website

A little bit about ourselves:
Bramwell College is a multicultural K-12 school with students who represent nearly 30 ethnic and cultural backgrounds. It is one of the fastest growing schools in the City of Torvale (in Perth, Western Australia), and offers quality education with a unique school environment at two campuses.
The mission of Bramwell College is to equip students with moral values, academic knowledge and 21st century skills. We empower students to unlock their potential to be confident global citizens.
Bramwell College strives to educate students in a manner which inspires them to become lifelong learners. We are committed to raising individuals who are tolerant and respectful towards others enabling them to grow into citizens who contribute to the common good of society.
Here are our design goals:
#1: To emphasise the growth of the school from a small school community to a much larger prestigious college.
#2: Have current and prospective parents have a clear understanding of our college’s morals and values and how we differ from other colleges.
#3: Highlight that our school provides a joyful and safe environment, which is highly valued by parents.
#4: Emphasise that our school presents a welcoming atmosphere for parents as we have strong relationships with our community.
#5: Highlight the various after-school activities available to our students, which are provided through the clubs and pastoral care department.
#6: Allow for online registrations and the option of adding student, staff and parent portals.
#7: Follow the existing school colours
We would like to request the design for the home page and a secondary page to see the alternative layouts.
Other information:
Please note that our logo is will be changed slightly in the upcoming weeks. Please keep this in mind while designing.
We will have another contest for the coding of the website.
We want to be able to make amendments and additions to the content of the website in the future and would like to make sure we have a strong communication with the designer.
The existing website is https://www.bramwellcol.example.edu.au/ for reference for school colours and content.
Industry/Entity Type
Education
Number of Pages Required
1 page

```html
<!DOCTYPE html>
<html lang="en">
<head>
<meta charset="utf-8">
<title>Bramwell College</title>
<link href="https://fonts.googleapis.com/css2?family=Figtree:wght@400;500;600;700&display=swap" rel="stylesheet">
<style>
:root{
  --ink:#111;
  --muted:#444;
  --sky:#2a9ee0;
  --royal:#1a56b2;
  --topbar:#0d0d0d;
  --footer:#2b2b2b;
  --faq:#ebebeb;
  --white:#fff;
}
*{box-sizing:border-box;margin:0;padding:0}
html,body{width:1200px;height:2676px;overflow:hidden}
body{font-family:"Figtree",Arial,sans-serif;color:var(--ink);background:var(--white);position:relative}
.abs{position:absolute}
.topbar{left:0;top:0;width:1200px;height:25px;background:var(--topbar);color:#ddd;font-size:11px}
.topbar .phone{left:95px;top:6px;display:flex;gap:8px;align-items:center}
.topbar .mail{left:521px;top:6px;display:flex;gap:8px;align-items:center}
.topbar .social{right:98px;top:6px;display:flex;gap:6px}
.dot{width:13px;height:13px;border-radius:50%;background:#eee;display:block}
.header{left:0;top:25px;width:1200px;height:75px;background:var(--white);border-bottom:1px solid #e4e4e4}
.brand{display:flex;align-items:center;gap:7px;font-weight:700;font-size:17px;color:var(--royal)}
.brand .mark{width:18px;height:18px;background:var(--sky)}
.header .brand{left:100px;top:28px}
.nav{left:288px;top:31px;display:flex;gap:19px;font-size:11.5px;font-weight:600}
.search{left:869px;top:25px;width:150px;height:24px;display:flex}
.search span{flex:1;background:#e6e6e6;font-size:10px;padding:6px 12px;color:#333}
.search b{width:36px;background:var(--sky);display:flex;align-items:center;justify-content:center}
.login{left:1050px;top:30px;font-size:11.5px;font-weight:600;color:var(--sky);display:flex;gap:6px;align-items:center}
.hero{left:0;top:100px;width:1200px;height:425px;background:linear-gradient(100deg,#6b3a2c 0%,#b08a78 30%,#c9a790 50%,#7a5550 70%,#2d2d33 85%,#8a3030 100%)}
.arrow{width:40px;height:40px;background:rgba(150,150,150,.75);display:flex;align-items:center;justify-content:center}
.hero .prev{left:100px;top:162px}
.hero .next{left:1060px;top:162px}
.dots{left:509px;top:381px;display:flex;gap:6px}
.dots i{width:12px;height:12px;border-radius:50%;background:#ddd;display:block}
.dots i.on{background:var(--sky)}
h2{font-size:21px;font-weight:700;text-align:center}
h2 em{font-style:normal;color:var(--sky)}
.campus-title{top:570px;width:368px}
.campus-photo{top:625px;width:369px;height:245px}
.announce-title{left:0;top:914px;width:1200px}
.card{width:178px;background:var(--white);box-shadow:0 2px 8px rgba(0,0,0,.12);top:985px;height:264px}
.card .pic{height:135px}
.card.raised .pic{height:96px}
.card .body{padding:12px 13px}
.card h3{font-size:12px;font-weight:700;margin-bottom:10px}
.card p{font-size:10.5px;line-height:1.3;color:#222}
.btn{display:inline-block;background:var(--sky);color:var(--white);font-size:11px;font-weight:600;border-radius:16px;padding:9px 16px;margin-top:14px}
.band{left:0;top:1311px;width:1200px;height:475px;background:var(--royal)}
.action{top:77px;width:238px;height:321px;border:2px solid var(--white);color:var(--white);padding:0 18px;display:flex;flex-direction:column;justify-content:center}
.action.solid{background:var(--white);color:var(--ink);box-shadow:0 4px 12px rgba(0,0,0,.25)}
.action h3{font-size:14.5px;font-weight:700;margin-bottom:12px}
.action p{font-size:11.7px;line-height:1.6}
.action .btn{align-self:flex-start}
.faq-title{left:0;top:1830px;width:1200px;font-size:19px}
.faq{left:321px;width:559px;height:37px;background:var(--faq);border-radius:3px;display:flex;align-items:center;justify-content:space-between;padding:0 20px 0 37px;font-size:10.8px;font-weight:600}
.faq-answer{left:358px;top:1953px;width:470px;font-size:10.5px;line-height:1.6;color:#333}
.footer{left:0;top:2372px;width:1200px;height:304px;background:var(--footer);color:#eee}
.footer .brand{left:225px;top:55px;color:var(--sky);font-size:18px}
.footer .social{left:225px;top:119px;display:flex;gap:13px}
.footer .social i{width:21px;height:21px;border-radius:50%;border:2px solid #fff;display:block}
.fhead{font-size:11.5px;color:var(--sky);font-weight:500}
.flinks{font-size:11px;line-height:39px}
.news{left:750px;top:57px;width:226px}
.news p{font-size:10.5px;margin:6px 0 12px;line-height:1.3}
.news .form{display:flex;height:31px}
.news .form span{flex:1;background:#eee;color:#444;font-size:12px;padding:8px 18px}
.news .form b{width:87px;background:var(--sky);color:#fff;font-size:12px;display:flex;align-items:center;justify-content:center}
.rule{left:225px;top:266px;width:750px;height:1px;background:#555}
.legal-row{top:281px;font-size:9.5px;letter-spacing:-.2px}
</style>
</head>
<body>
<div class="abs topbar">
  <div class="abs phone"><svg width="10" height="10" viewBox="0 0 24 24"><path fill="#ddd" d="M6.6 10.8a15 15 0 0 0 6.6 6.6l2.2-2.2c.3-.3.7-.4 1-.2 1.1.4 2.3.6 3.6.6.6 0 1 .4 1 1V20c0 .6-.4 1-1 1A17 17 0 0 1 3 4c0-.6.4-1 1-1h3.5c.6 0 1 .4 1 1 0 1.3.2 2.5.6 3.6.1.3 0 .7-.2 1z"/></svg>1-800-555-0142</div>
  <div class="abs mail"><svg width="10" height="8" viewBox="0 0 20 14"><rect width="20" height="14" fill="#ddd"/><path d="M0 0l10 8 10-8" stroke="#0d0d0d" fill="none" stroke-width="1.5"/></svg>hello@bramwellcol.example.edu.au</div>
  <div class="abs social"><i class="dot"></i><i class="dot"></i><i class="dot"></i><i class="dot"></i></div>
</div>

<header class="abs header">
  <div class="abs brand"><span class="mark"></span>Bramwell College</div>
  <nav class="abs nav"><span>About Us</span><span>Learning</span><span>Student Life</span><span>Enrolment</span><span>Community</span><span>News &amp; Events</span><span>Contact Us</span></nav>
  <div class="abs search"><span>Search</span><b><svg width="12" height="12" viewBox="0 0 24 24"><circle cx="10" cy="10" r="7" stroke="#fff" stroke-width="2.5" fill="none"/><path d="M15 15l6 6" stroke="#fff" stroke-width="2.5"/></svg></b></div>
  <div class="abs login">Log In <svg width="16" height="14" viewBox="0 0 16 14"><path d="M10 1h5v12h-5" stroke="#2a9ee0" stroke-width="1.6" fill="none"/><path d="M1 5h5V2l6 5-6 5V9H1z" fill="#2a9ee0"/></svg></div>
</header>

<section class="abs hero" role="img" aria-label="Photo of smiling young students in costume waving">
  <div class="abs arrow prev"><svg width="26" height="20" viewBox="0 0 26 20"><path d="M25 10H3M11 2 3 10l8 8" stroke="#fff" stroke-width="2.4" fill="none"/></svg></div>
  <div class="abs arrow next"><svg width="26" height="20" viewBox="0 0 26 20"><path d="M1 10h22M15 2l8 8-8 8" stroke="#fff" stroke-width="2.4" fill="none"/></svg></div>
  <div class="abs dots"><i></i><i></i><i class="on"></i><i></i><i></i></div>
</section>

<h2 class="abs campus-title" style="left:225px">Ferndale <em>Campus</em></h2>
<h2 class="abs campus-title" style="left:606px">Lynwood <em>Campus</em></h2>
<div class="abs campus-photo" style="left:225px;background:linear-gradient(180deg,#c9d3dc 0%,#a89a8c 45%,#6a7c3e 70%,#4f6a2c 100%)" role="img" aria-label="Ferndale campus buildings with lawn and brick path"></div>
<div class="abs campus-photo" style="left:606px;background:linear-gradient(180deg,#2a6fd0 0%,#6aa0df 35%,#8a4a3a 55%,#4d8a2c 75%,#3c7424 100%)" role="img" aria-label="Lynwood campus brick building under blue sky"></div>

<h2 class="abs announce-title">Announcements</h2>
<article class="abs card" style="left:225px">
  <div class="pic" style="background:linear-gradient(135deg,#8a6a5a,#4a5a8a,#c8b8a8)" role="img" aria-label="Students seated on a classroom floor raising hands"></div>
  <div class="body"><h3>Open House Day</h3><p>Join us for our Open House Day and experience firsthand the vibrant learning community at Bramwell College.</p></div>
</article>
<article class="abs card raised" style="left:416px;top:985px">
  <div class="pic" style="background:linear-gradient(180deg,#dfe3e6,#8a7a6a,#b9aea2)" role="img" aria-label="Empty classroom with rows of desks"></div>
  <div class="body"><h3>Open House Day</h3><p>Join us for our Open House Day and experience firsthand the vibrant learning community at Bramwell College.</p><span class="btn">Learn More</span></div>
</article>
<article class="abs card" style="left:606px">
  <div class="pic" style="background:linear-gradient(135deg,#e4e4e4,#9a8a7a,#3a8a4a)" role="img" aria-label="Students working at desks in a classroom"></div>
  <div class="body"><h3>Open House Day</h3><p>Join us for our Open House Day and experience firsthand the vibrant learning community at Bramwell College.</p></div>
</article>
<article class="abs card" style="left:797px">
  <div class="pic" style="background:linear-gradient(180deg,#e8d8b8,#b8602c,#d8c8a8)" role="img" aria-label="Rows of wooden desks in a bright room"></div>
  <div class="body"><h3>Open House Day</h3><p>Join us for our Open House Day and experience firsthand the vibrant learning community at Bramwell College.</p></div>
</article>

<section class="abs band">
  <div class="abs action" style="left:225px"><h3>Book a Tour</h3><p>Discover the welcoming atmosphere and exceptional facilities of Bramwell College by booking a personalized campus tour. Our friendly staff will guide you through our classrooms, laboratories, and recreational areas, providing insights into our educational programs.</p><span class="btn">Book Now</span></div>
  <div class="abs action solid" style="left:481px"><h3>Enrollment Application Form</h3><p>Ready to take the next step? Complete our enrollment application form to secure a place for your child at Bramwell College. Our inclusive community fosters academic excellence, personal growth, and a strong sense of belonging.</p><span class="btn">Enroll Now</span></div>
  <div class="abs action" style="left:737px"><h3>Prospectus</h3><p>Explore the Bramwell College Prospectus to learn more about our esteemed institution. Inside, you'll find detailed information about our curriculum, extracurricular activities, faculty, and the unique opportunities we offer.</p><span class="btn">Let's explore</span></div>
</section>

<h2 class="abs faq-title">Frequently Asked Questions</h2>
<div class="abs faq" style="top:1902px">What are the admission requirements at Bramwell College? <svg width="12" height="12"><path d="M0 6h12" stroke="#111" stroke-width="2"/></svg></div>
<p class="abs faq-answer">We welcome students from diverse backgrounds. To join Bramwell College, please refer to our Admissions page for detailed information on the application process, age requirements, necessary documents, and any specific criteria for different grade levels.</p>
<div class="abs faq" style="top:2022px">What is the curriculum offered at Bramwell College? <svg width="12" height="12"><path d="M0 6h12M6 0v12" stroke="#111" stroke-width="2"/></svg></div>
<div class="abs faq" style="top:2078px">Are there any after-school activities available for students? <svg width="12" height="12"><path d="M0 6h12M6 0v12" stroke="#111" stroke-width="2"/></svg></div>
<div class="abs faq" style="top:2134px">What support services are available for students' well-being? <svg width="12" height="12"><path d="M0 6h12M6 0v12" stroke="#111" stroke-width="2"/></svg></div>
<div class="abs faq" style="top:2190px">How can parents stay involved and engaged with the school community? <svg width="12" height="12"><path d="M0 6h12M6 0v12" stroke="#111" stroke-width="2"/></svg></div>
<div class="abs faq" style="top:2246px">What are the facilities like at Bramwell College? <svg width="12" height="12"><path d="M0 6h12M6 0v12" stroke="#111" stroke-width="2"/></svg></div>

<footer class="abs footer">
  <div class="abs brand"><span class="mark"></span>Bramwell College</div>
  <div class="abs social"><i></i><i></i><i></i><i></i></div>
  <div class="abs fhead" style="left:402px;top:57px">NAVIGATIONS</div>
  <div class="abs flinks" style="left:402px;top:78px">About Us<br>Learning<br>Student Life<br>Enrolment</div>
  <div class="abs flinks" style="left:473px;top:78px;padding-left:18px">Community<br>News &amp; Events<br><span style="padding-left:20px">Contact Us</span></div>
  <div class="abs fhead" style="left:600px;top:57px">LEGAL</div>
  <div class="abs flinks" style="left:600px;top:78px">Information Ribbon<br>Disclaimer<br>Acknowledgement</div>
  <div class="abs news"><div class="fhead">NEWSLETTER</div><p>Join Our News Letter To Stay Up To Dated With Our Latest Updates</p><div class="form"><span>Enter Email</span><b>Submit</b></div></div>
  <div class="abs rule"></div>
  <div class="abs legal-row" style="left:225px">All Rights Reserved</div>
  <div class="abs legal-row" style="left:553px">© 2023, Northgate Studio</div>
  <div class="abs legal-row" style="left:832px">Terms Conditions | Privacy &amp; Policy</div>
</footer>
</body>
</html>
```